Painting Company Business Card

Brightwell Painting needs a new business card. See attachments for our logo and current card as an example.
We want to utilize the same colors in the logo, and keep all the information that is currently on it. Just need an updated and modern design.
We are open to loosing the Association Logos if it means a better design.
We are also entertaining a spot for a picture of a headshot of the person listed on the card. Head shot can be finished later.

```html
<!DOCTYPE html>
<html lang="en">
<head>
<meta charset="utf-8">
<title>Brightwell Painting – Business Card</title>
<link rel="stylesheet" href="https://fonts.googleapis.com/css2?family=Lato:wght@400;700&display=swap">
<style>
  :root {
    --backdrop: #555555;
    --paper: #ffffff;
    --forest: #344a30;
    --maroon: #6e3535;
    --ink-light: #ffffff;
    --photo-dark: #1f2430;
    --photo-light: #e9e4e0;
  }
  * { box-sizing: border-box; margin: 0; padding: 0; }
  html, body {
    width: 1200px; height: 900px; overflow: hidden;
    background: var(--backdrop);
    font-family: "Lato", sans-serif;
  }
  .stage { position: relative; width: 1200px; height: 900px; }

  .card {
    position: absolute; top: 200px; width: 310px; height: 502px; overflow: hidden;
    background: var(--paper);
  }
  .card-front { left: 253px; border-radius: 46px 0 46px 0; }
  .card-back  { left: 627px; border-radius: 0 46px 0 46px; }

  .headshot {
    position: absolute; inset: 0;
    background: linear-gradient(180deg, var(--photo-light) 0%, var(--photo-light) 45%, #b79a87 55%, var(--photo-dark) 75%, var(--photo-dark) 100%);
  }
  .person {
    position: absolute; left: 0; right: 0; bottom: 43px; text-align: center; color: var(--ink-light);
  }
  .person-name { font-weight: 700; font-size: 20px; letter-spacing: 1px; line-height: 22px; }
  .person-role { font-size: 15px; line-height: 18px; }

  .brand {
    position: absolute; top: 0; left: 0; right: 0; height: 243px;
    display: flex; align-items: center; justify-content: center; gap: 10px;
  }
  .brand-mark { width: 14px; height: 14px; border-radius: 50%; background: var(--forest); }
  .brand-name { font-weight: 700; font-size: 27px; color: var(--forest); }

  .contact-band {
    position: absolute; top: 243px; left: 0; right: 0; height: 129px;
    background: var(--forest); color: var(--ink-light); text-align: center;
  }
  .icon-row {
    position: absolute; top: 22px; left: 74px; width: 162px; height: 22px;
  }
  .contact-list {
    position: absolute; top: 55px; left: 0; right: 0; font-size: 14.5px; line-height: 18px;
  }
  .services-band {
    position: absolute; top: 377px; left: 0; right: 0; bottom: 0;
    background: var(--maroon); color: var(--ink-light); text-align: center;
    padding-top: 29px; font-size: 14.5px; line-height: 18px;
  }
  .dot { display: inline-block; width: 8px; height: 8px; border-radius: 50%; background: var(--ink-light); margin: 0 8px 1px; }
</style>
</head>
<body>
<main class="stage">
  <section class="card card-front">
    <div class="headshot" role="img" aria-label="Headshot of Mark Ellison in a dark suit and red tie"></div>
    <div class="person">
      <p class="person-name">MARK ELLISON</p>
      <p class="person-role">Quality Manager</p>
    </div>
  </section>

  <section class="card card-back">
    <div class="brand">
      <span class="brand-mark"></span>
      <span class="brand-name">Brightwell Painting</span>
    </div>

    <div class="contact-band">
      <svg class="icon-row" viewBox="0 0 162 22" aria-hidden="true">
        <line x1="0" y1="11" x2="46" y2="11" stroke="#8a9a86" stroke-width="1"/>
        <line x1="116" y1="11" x2="162" y2="11" stroke="#8a9a86" stroke-width="1"/>
        <circle cx="58" cy="11" r="10" fill="#fff"/>
        <circle cx="81" cy="11" r="10" fill="#fff"/>
        <circle cx="104" cy="11" r="10" fill="#fff"/>
        <path d="M53 9 q5 -4 10 0 l-1 2 h-2 v-1 h-4 v1 h-2 z M54 12 h8 v3 h-8 z" fill="#344a30"/>
        <rect x="75.5" y="7" width="11" height="8" fill="#344a30"/>
        <path d="M75.5 7 l5.5 4.5 l5.5 -4.5" fill="none" stroke="#fff" stroke-width="1"/>
        <circle cx="104" cy="11" r="5.5" fill="none" stroke="#344a30" stroke-width="1.5"/>
        <path d="M98.5 11 h11 M104 5.5 v11" stroke="#344a30" stroke-width="1"/>
      </svg>
      <div class="contact-list">
        <p>262-555-0147</p>
        <p>mark.Brightwell@mailbox.com</p>
        <p>www.BrightwellPainting.com</p>
      </div>
    </div>

    <div class="services-band">
      <p>Exterior Painting</p>
      <p>Interior Painting</p>
      <p>Carpentry<span class="dot"></span>Drywall</p>
    </div>
  </section>
</main>
</body>
</html>
```